Innovative Webpage for leadership development and training company

Bright Harbour is a company supporting small organisations, in particular NGOs or projects, to increase the impact of their training and to increase the retention of talent through customized leadership development solutions. We help organisations to Guide Well & Coach Well
We want to have a simple but modern design webpage that stands outs from the usual consulting webpages
Here you are two possible examples of consulting firms approaching the same target audience
http://www.quillmarsh.eu/
http://borvencast.com/#intro
The webpage should be designed and developed in a platform that allows full customization in the future both in terms of pages, text and images
It should allow the integration of two short videos that are currently under development
It should allow the maximum possible interoperabililty with tables and smartphones

Target Market(s)

Nonprofit, young professionals, technical assistance and capacity building projects, global SMEs, multicultural teals

Industry/Entity Type

Leadership

Number of Pages Required

5+ page

Requirements
Must have
• A dynamic/engaging/modern homepage
• A design that can be easily transferable to other pages
• A user-friendly platform that allows complete customization
• Evaluation Criteria
• 1. Overall Design/Feel of the webpage (in particular homepage). Our company looks for innovative leadership development and training. We often step out of our comfort zone in a playful positive way and that requires courage.
• 2. Flexibility to edit and/or translate homepage design to new/other pages
• 3. User-friendliness to customize, change the webpage
• 4. Completeness of coded pages (# of pages effectively developed)
Nice to have
• The maximum number of coded pages designed as per the attached file

```html
<!DOCTYPE html>
<html lang="en">
<head>
<meta charset="utf-8">
<title>Bright Harbour — Leadership Development</title>
<link href="https://fonts.googleapis.com/css2?family=Raleway:wght@200;300;400;500;600;700&family=Open+Sans:ital,wght@0,400;0,600;1,400&display=swap" rel="stylesheet">
<style>
:root{
  --blue:#1a8ad6;
  --blue-deep:#0d6fc6;
  --orange:#f47a20;
  --gold:#f5a623;
  --ink:#222;
  --text:#666;
  --grey-band:#dedede;
  --light-band:#ececec;
  --chirp:#0aa3e8;
  --bar:#333;
  --footer:#1b1b1b;
  --white:#fff;
}
*{margin:0;padding:0;box-sizing:border-box}
html,body{width:1200px;height:3371px;overflow:hidden}
body{position:relative;background:var(--white);font-family:'Open Sans',Arial,sans-serif;color:var(--text)}
.abs{position:absolute}
.heading{font-family:'Raleway',Arial,sans-serif;font-weight:400;text-align:center;left:0;width:1200px}

/* header */
.site-header{top:0;left:0;width:1200px;height:110px;background:var(--white)}
.brand{left:158px;top:22px;display:flex;align-items:center;gap:10px}
.brand-dot{width:34px;height:34px;border-radius:50%;background:var(--orange)}
.brand-name{font-family:'Raleway',sans-serif;font-weight:700;font-size:22px;color:var(--ink);line-height:1}
.main-nav{right:160px;top:44px;display:flex;gap:44px;font-size:11px;color:#444}
.main-nav a{color:inherit;text-decoration:none;position:relative}
.main-nav .active{color:var(--gold)}
.main-nav .active::after{content:"";position:absolute;left:0;right:0;bottom:-10px;height:2px;background:var(--gold)}

/* hero */
.hero{top:112px;left:0;width:1200px;height:598px;background:linear-gradient(120deg,#c9ccd2 0%,#e9e9ea 40%,#b9b5b2 70%,#8d8580 100%)}
.hero-box{left:348px;top:243px;width:438px;height:117px;background:rgba(255,255,255,.78);text-align:center;padding-top:12px}
.hero-box h1{font-family:'Raleway',sans-serif;font-weight:300;font-size:40px;color:var(--orange);line-height:1.1}
.hero-box p{font-size:13px;color:#555;line-height:1.4;margin-top:4px}

/* welcome */
.welcome-title{top:762px;font-size:30px;color:var(--blue)}
.welcome-title b{color:var(--ink);font-weight:700}
.welcome-title span{color:var(--ink);font-size:22px}
.welcome-text{top:818px;left:350px;width:500px;font-size:11px;line-height:1.6;text-align:center}

/* about */
.about{left:162px;top:910px;width:400px}
.about h2{font-family:'Raleway',sans-serif;font-weight:600;font-size:22px;color:var(--blue)}
.about h2::after{content:"";display:block;width:40px;height:2px;background:var(--blue);margin-top:14px}
.about h3{font-family:'Raleway',sans-serif;font-weight:500;font-size:16px;color:var(--ink);margin-top:16px}
.about p{font-size:11px;line-height:1.6;margin-top:28px}
.btn{display:inline-block;font-size:10px;color:var(--white);text-align:center;font-weight:600}
.btn-blue{background:var(--blue);width:120px;height:36px;line-height:36px;margin-top:28px}
.about-photo{left:602px;top:892px;width:436px;height:270px;background:linear-gradient(135deg,#e6e8ec,#b3b8c2 60%,#5d6470)}

/* video */
.video-title{top:1214px;font-size:29px;color:var(--gold)}
.video-title b{font-weight:700}
.video-band{top:1290px;left:0;width:1200px;height:472px;background:var(--grey-band)}
.video-frame{left:162px;top:1339px;width:876px;height:373px;border:3px solid var(--gold);background:linear-gradient(120deg,#2b2b2b,#1c1c1c 50%,#262626)}
.video-play{left:560px;top:1500px;width:78px;height:54px;border-radius:10px;background:var(--gold)}

/* services */
.services-title{top:1812px;font-size:30px;color:var(--orange);font-weight:500}
.service{width:300px;text-align:center}
.service-photo{width:190px;height:190px;border-radius:50%;margin:0 auto;background:linear-gradient(135deg,#e7e9ed,#9aa0aa)}
.service-photo.ring{border:3px solid var(--orange)}
.service h4{font-family:'Open Sans',sans-serif;font-weight:400;font-size:14px;color:var(--ink);margin-top:16px}
.service h4.accent{color:var(--orange)}
.service p{font-size:9.5px;line-height:1.55;width:240px;margin:6px auto 0}
.btn-small{width:74px;height:27px;line-height:27px;font-size:8.5px;margin-top:14px}
.btn-dark{background:#111}
.btn-orange{background:var(--orange)}

/* clients */
.clients-title{top:2284px;font-size:30px;color:var(--gold);font-weight:400}
.clients-title b{color:var(--gold);font-weight:700}
.clients-text{top:2336px;left:350px;width:500px;font-size:11px;line-height:1.6;text-align:center}
.client-arrows{left:1016px;top:2396px}
.client-strip{left:162px;top:2420px;width:876px;height:146px;border:1px solid #ddd;display:flex;align-items:center;justify-content:space-around;padding:0 10px}
.client{display:flex;align-items:center;gap:10px;font-family:'Open Sans',sans-serif;font-weight:600;font-size:19px;color:#1d3f7a}
.client i{width:22px;height:22px;background:#1d3f7a;display:block}

/* testimonials */
.testi-band{top:2629px;left:0;width:1200px;height:463px;background:var(--light-band)}
.testi-title{top:2682px;font-size:30px;color:var(--blue-deep);font-weight:500}
.card{top:2789px;width:288px;height:233px;background:var(--white);box-shadow:0 1px 3px rgba(0,0,0,.15)}
.card blockquote{font-style:italic;font-size:10px;line-height:1.55;color:#333;text-align:center;padding:24px 20px 0}
.card .quote-mark{font-family:Georgia,serif;font-size:26px;color:var(--blue-deep);position:absolute;left:14px;top:6px;line-height:1}
.card-foot{position:absolute;left:-4px;right:0;bottom:0;height:83px;background:var(--blue-deep);display:flex;align-items:center;padding-left:18px;gap:14px;color:var(--white)}
.avatar{width:58px;height:58px;border-radius:50%;border:3px solid var(--white);background:linear-gradient(135deg,#d8d2cc,#8c8580);flex:none}
.card-foot strong{font-size:12px;font-weight:600;display:block}
.card-foot small{font-size:8.5px;line-height:1.4;display:block;margin-top:4px}

/* social */
.social-bar{top:3094px;left:0;width:1200px;height:74px;background:var(--bar)}
.social{top:3094px;height:74px;width:292px;display:flex;align-items:center;justify-content:center;gap:12px;font-size:13px;color:#ddd}
.social.chirp{background:var(--chirp);color:var(--white);font-weight:600}
.social .dot{width:12px;height:12px;border-radius:50%;background:currentColor}

/* footer */
.site-footer{top:3168px;left:0;width:1200px;height:203px;background:var(--footer)}
.footer-brand{top:3230px;left:0;width:1200px;display:flex;justify-content:center;align-items:center;gap:10px;opacity:.35}
.footer-brand .brand-dot{background:#999}
.footer-brand .brand-name{color:#bbb}
.copyright{top:3336px;left:0;width:1200px;text-align:center;font-size:10px;color:#666}
</style>
</head>
<body>

<header class="site-header abs">
  <div class="brand abs"><span class="brand-dot"></span><span class="brand-name">Bright Harbour</span></div>
  <nav class="main-nav abs">
    <a class="active" href="#">Home</a><a href="#">About Us</a><a href="#">Services</a><a href="#">Testimonials</a><a href="#">Blog</a><a href="#">Contact Us</a>
  </nav>
</header>

<section class="hero abs" role="img" aria-label="Team meeting photo with a presenter at a flip chart">
  <div class="hero-box abs">
    <h1>Hello We Are !</h1>
    <p>Bright Harbour Sprl. offers tailor-made innovative solutions<br>for organisational andindividual excellence.</p>
  </div>
</section>

<h2 class="heading welcome-title abs">Welcome to <b>Bright Harbour</b> <span>Development</span></h2>
<p class="welcome-text abs">Bright Harbour Sprl. offers tailor-made innovative solutions for organisational and individual excellence. We strive to transform the capacity...</p>

<div class="about abs">
  <h2>About Us</h2>
  <h3>Mission Statement</h3>
  <p>We share innovation, inspiration and collaborative partnership to our clients to support their learning and development capacity and increase the impact of their projects and initiatives.</p>
  <a class="btn btn-blue">Read More</a>
</div>
<div class="about-photo abs" role="img" aria-label="Training session photo with a trainer at a whiteboard"></div>

<h2 class="heading video-title abs">View Our <b>Training Video</b></h2>
<div class="video-band abs"></div>
<div class="video-frame abs" role="img" aria-label="Dimmed video still of a team meeting"></div>
<svg class="video-play abs" viewBox="0 0 78 54"><rect width="78" height="54" rx="10" fill="#f5a623"/><path d="M31 15 L53 27 L31 39 Z" fill="#111"/></svg>

<h2 class="heading services-title abs">Our Services</h2>
<div class="service abs" style="left:149px;top:1883px">
  <div class="service-photo ring" role="img" aria-label="Business people at a desk"></div>
  <h4 class="accent">Organisational Development</h4>
  <p>Bright Harbour's leadership and management development programs help managers develop themselves...</p>
  <a class="btn btn-small btn-dark">Read More</a>
</div>
<div class="service abs" style="left:450px;top:1883px">
  <div class="service-photo" role="img" aria-label="Coach presenting at a flip chart"></div>
  <h4>Executive Coaching</h4>
  <p>Bright Harbour's coaching programs, which are either face-to-face or by Talkmere, help middle managers and senior leaders...</p>
  <a class="btn btn-small btn-orange">Read More</a>
</div>
<div class="service abs" style="left:749px;top:1883px">
  <div class="service-photo" role="img" aria-label="Group training at a whiteboard"></div>
  <h4>Training</h4>
  <p>His experience includes coaching senior leaders working in multicultural teams in banking, insurance, international trade...</p>
  <a class="btn btn-small btn-orange">Read More</a>
</div>

<h2 class="heading clients-title abs">Our <b>Clients</b></h2>
<p class="clients-text abs">Non-profit organisations Many NGOs have an international or global mandate supported by a slim organizational structure.</p>
<svg class="client-arrows abs" width="22" height="14" viewBox="0 0 22 14"><path d="M7 2 L2 7 L7 12" stroke="#f5a623" stroke-width="2" fill="none"/><path d="M15 2 L20 7 L15 12" stroke="#333" stroke-width="2" fill="none"/></svg>
<div class="client-strip abs">
  <span class="client"><i></i>Ridgeline Civic Alliance</span>
  <span class="client">Larkspur for Causes</span>
  <span class="client"><i></i>Kitami Vale</span>
  <span class="client">Clearview Aid</span>
</div>

<div class="testi-band abs"></div>
<h2 class="heading testi-title abs">Testimonials</h2>
<article class="card abs" style="left:157px">
  <span class="quote-mark">&ldquo;</span>
  <blockquote>I have been impressed by Aren's capacity to coach and train high-level government officials with success. My reports show he has been able to increase their motivation in increasing their capacities of driving complex change management processes.</blockquote>
  <div class="card-foot"><span class="avatar" role="img" aria-label="Portrait of the client"></span><div><strong>Mr. LV</strong><small>Business Development in Emerging<br>Markets, Spain</small></div></div>
</article>
<article class="card abs" style="left:458px">
  <span class="quote-mark">&ldquo;</span>
  <blockquote>Aren's professionalism and dedication to his field is remarkable as is his strength and confidence as a coach. A careful listener, Mr. Tarrow helped each of the training participants individually and uniquely, focused on developing confident skilled coaches</blockquote>
  <div class="card-foot"><span class="avatar" role="img" aria-label="Portrait of the client"></span><div><strong>Mr. SR</strong><small>Training Director, Executive Search and<br>HR Consulting, China</small></div></div>
</article>
<article class="card abs" style="left:760px">
  <span class="quote-mark">&ldquo;</span>
  <blockquote>I have been impressed by Aren's capacity to coach and train high-level government officials with success. My reports show he has been able to increase their motivation in increasing their capacities of driving complex change management processes.</blockquote>
  <div class="card-foot"><span class="avatar" role="img" aria-label="Portrait of the client"></span><div><strong>Mr. LV</strong><small>Business Development in Emerging<br>Markets, Spain</small></div></div>
</article>

<div class="social-bar abs"></div>
<a class="social abs" style="left:162px"><span class="dot"></span>Friendwall</a>
<a class="social chirp abs" style="left:454px"><span class="dot"></span>Chirper</a>
<a class="social abs" style="left:746px"><span class="dot"></span>Orbit Plus</a>

<footer class="site-footer abs"></footer>
<div class="footer-brand abs"><span class="brand-dot"></span><span class="brand-name">Bright Harbour</span></div>
<p class="copyright abs">© All Copyrights Reserved 2015</p>

</body>
</html>
```